Wine Label for my husband’s 50th birthday party

I need a wine label to celebrate my husband’s 50th birthday. We are having a large party for approx 100 guests. My husband is a very proud Wine Grape Grower in The Riverland, South Australia and one of the wineries he supplies has made these wines for him, especially to be consumed at the party - so maybe that they are his grapes can be included in/on the label? His name is Nikos, so maybe incorporate that into the label - Nikos’s Harvest? The Nikos, Exclusive and Limited Release? Label might include his year of birth 1968, eg good year?
There will be various varieties of wine, I will update with the details as soon as I get them. So we may actually need more than 1 label....
The date of the party is 5th May 2018.
My hubby is Greek, is a Greek theme, or Greek gods, Greek mythology might be included?
The photo uploads below are some that I like and that catch my eye.

Target Market(s)

45-55yo

Colors

Designer to choose colors to be used in the design.

Requirements
Must have
• I love some of the quirky wine labels now! Must include my husband’s name, Nikos. Perhaps year of birth 1968. Greek theme, mythology, gods etc
Nice to have
• Bright pops of colour. Maybe a Greek theme, perhaps using the variety and Greek god name or theme - Eg Cyclops Cabernet, Hydra Grenache etc
Should not have
• Grapes, vines, boring colours.

```html
<!DOCTYPE html>
<html lang="en">
<head>
<meta charset="utf-8">
<title>Nikos’s Harvest – Merlo Label</title>
<link rel="stylesheet" href="https://fonts.googleapis.com/css2?family=Tinos:wght@400;700&display=swap">
<style>
  :root {
    --page: #ffffff;
    --paper: #f1f1df;
    --ink-navy: #252e45;
    --wine-red: #a8191a;
    --figure-bronze: #846b40;
    --wash-lilac: #c9c6d6;
    --wash-berry: #a64246;
    --wash-red: #c2282a;
    --wash-mint: #cbdcc8;
    --wash-sand: #d6c39c;
    --wash-yellow: #e6dd8a;
    --wash-salmon: #e7a08c;
    --wash-blush: #ecc6b4;
  }
  * { margin: 0; padding: 0; box-sizing: border-box; }
  html, body {
    width: 1200px; height: 1200px; overflow: hidden;
    background: var(--page);
  }
  .label {
    position: absolute;
    left: 277px; top: 238px;
    width: 631px; height: 706px;
    background: var(--paper);
    box-shadow: 0 8px 18px rgba(0,0,0,0.18);
    overflow: hidden;
    font-family: "Tinos", serif;
    color: var(--ink-navy);
  }
  .label__wash {
    position: absolute;
    left: 279px; top: 0;
    width: 352px; height: 100%;
    background:
      radial-gradient(ellipse 60% 22% at 85% 8%, var(--wash-berry) 0%, var(--wash-red) 45%, transparent 75%),
      linear-gradient(180deg,
        var(--wash-lilac) 0%,
        var(--wash-mint) 22%,
        var(--wash-sand) 38%,
        var(--wash-yellow) 52%,
        var(--wash-salmon) 70%,
        var(--wash-blush) 100%);
    -webkit-mask-image: linear-gradient(90deg, transparent 0%, #000 35%);
    mask-image: linear-gradient(90deg, transparent 0%, #000 35%);
    opacity: 0.9;
  }
  .label__figure {
    position: absolute;
    left: 24px; top: 35px;
    width: 300px; height: 417px;
    border-radius: 40px;
    background: linear-gradient(180deg, rgba(132,107,64,0.55) 0%, var(--figure-bronze) 50%, rgba(132,107,64,0.55) 100%);
  }
  .label__edition {
    position: absolute;
    left: 371px; top: 338px;
    width: 180px;
    text-align: center;
  }
  .edition__word {
    display: block;
    font-size: 14px;
    font-weight: 400;
    letter-spacing: 4px;
    line-height: 18px;
  }
  .edition__year {
    display: block;
    font-size: 40px;
    font-weight: 400;
    line-height: 46px;
    letter-spacing: 2px;
  }
  .label__title {
    position: absolute;
    left: 46px; top: 462px;
    font-size: 92px;
    font-weight: 700;
    line-height: 82px;
    white-space: nowrap;
  }
  .label__variety {
    position: absolute;
    left: 48px; top: 627px;
    font-size: 26px;
    font-weight: 700;
    line-height: 28px;
    letter-spacing: 0.6em;
    color: var(--wine-red);
  }
  .label__specs {
    position: absolute;
    left: 401px; top: 660px;
    display: flex; align-items: center;
    font-size: 15px;
    line-height: 22px;
  }
  .specs__divider {
    width: 1px; height: 22px;
    background: rgba(37,46,69,0.25);
    margin: 0 17px 0 24px;
  }
</style>
</head>
<body>
  <main class="label">
    <div class="label__wash" role="img" aria-label="Watercolour wash in red, lilac, yellow and salmon tones"></div>
    <div class="label__figure" role="img" aria-label="Greek vase-painting style figure carrying a robe and offering a wine cup"></div>

    <p class="label__edition">
      <span class="edition__word">LIMITED</span>
      <span class="edition__year">( 1968 )</span>
      <span class="edition__word">RELEASE</span>
    </p>

    <h1 class="label__title">NIKOS’S<br>HARVEST</h1>
    <p class="label__variety">MERLO</p>

    <div class="label__specs">
      <span class="specs__alc">alc 13.0% vol</span>
      <span class="specs__divider"></span>
      <span class="specs__volume">750 ml</span>
    </div>
  </main>
</body>
</html>
```